WordPress Website for Pain Relief Clinic

I need a WordPress website designed for my laser pain relief clinic. It needs to be a professional, responsive design with 7 pages: Home, Why Choose Us, Treatable Conditions, Testimonials, FAQ, Franchising, Contact Us. Here is logo: https://files.brivoltcdn.com/media.t-w-e-n.com/sitebuilder/472/CalvexaLogoHighQuality.png

Target Market(s)

people with pain,elderly adults,injuries,soreness

Industry/Entity Type

Clinic

Number of Pages Required

5+ page

Colors
0792cd
85abd2

```html
<!DOCTYPE html>
<html lang="en">
<head>
<meta charset="utf-8">
<title>Calvexa – Laser Pain Relief Clinic</title>
<link rel="stylesheet" href="https://fonts.googleapis.com/css2?family=Montserrat:wght@400;600;700&family=Open+Sans:ital,wght@0,400;0,600;0,700;1,700&display=swap">
<style>
:root{
  --red:#d9302c;
  --red-dark:#b8221f;
  --red-text:#e2332f;
  --ink:#1e1e1e;
  --body:#555;
  --light:#f0f0f0;
  --white:#fff;
  --footer:#0f1613;
  --footer-text:#9aa3a0;
}
*{box-sizing:border-box;margin:0;padding:0}
html,body{width:1200px;height:2432px;overflow:hidden}
body{position:relative;font-family:"Open Sans",Arial,sans-serif;color:var(--body);background:var(--white)}
.abs{position:absolute}
h1,h2,h3,.brand,.nav,.btn{font-family:"Montserrat",Arial,sans-serif}

/* header */
.site-header{position:absolute;left:0;top:0;width:1200px;height:138px;background:var(--white);border-bottom:3px solid var(--red)}
.brand{position:absolute;left:172px;top:40px;display:flex;align-items:center;gap:12px;font-size:38px;font-weight:600;color:var(--ink)}
.brand-mark{width:22px;height:22px;background:var(--red)}
.top-links{position:absolute;right:237px;top:18px;font-size:11px;color:#555;display:flex;gap:10px;align-items:center}
.top-links span.sep{color:#bbb}
.call{position:absolute;right:237px;top:38px;font-size:16px;color:#555}
.call b{color:var(--ink)}
.nav{position:absolute;left:462px;top:82px;display:flex;gap:30px;align-items:center;font-size:13px;font-weight:600;color:var(--ink)}
.nav .active{color:var(--red)}
.nav .quote{background:var(--red);color:var(--white);padding:9px 16px;margin-left:0}

/* hero */
.hero{left:0;top:141px;width:1200px;height:376px;background:linear-gradient(100deg,#cfc9c0 0%,#e6e2dc 40%,#d6d8da 70%,#a9adb0 100%)}
.hero h1{position:absolute;left:0;width:1200px;top:84px;text-align:center;color:var(--red-text);font-size:36px;font-weight:700}
.hero .rule{position:absolute;left:555px;top:136px;width:90px;height:3px;background:var(--white)}
.hero p{position:absolute;left:340px;width:520px;top:170px;text-align:center;font-size:12px;line-height:20px;color:#333}
.hero .btn{left:544px;top:265px}
.dots{position:absolute;display:flex;gap:8px}
.dots i{width:10px;height:10px;border-radius:50%;border:2px solid var(--white);background:var(--white)}
.dots i.on{background:var(--red)}
.btn{position:absolute;background:var(--red);color:var(--white);font-size:12px;font-weight:600;padding:9px 26px}

/* service band */
.services{left:0;top:517px;width:1200px;height:304px;background:linear-gradient(135deg,#cf2b28,#e0403b 50%,#c72623)}
.card{position:absolute;top:73px;width:170px;height:170px;border:4px solid #b82522}
.card .photo{width:100%;height:100%;background:linear-gradient(160deg,#d9c4b3,#8f8178)}
.card span{position:absolute;left:0;bottom:0;width:100%;height:42px;background:rgba(30,30,30,.6);color:var(--white);font-size:12px;font-weight:600;text-align:center;line-height:42px}

/* why choose us */
.why-photo{left:0;top:821px;width:537px;height:355px;background:linear-gradient(120deg,#f3ebe6,#d8c3b5 55%,#f2f2f2)}
.section-title{font-size:30px;font-weight:600;color:var(--ink)}
.copy{font-size:11.5px;line-height:19px;color:var(--body)}
.copy b{color:var(--ink)}
.copy p+p{margin-top:17px}

/* quote */
.quote-band{left:0;top:1176px;width:1200px;height:77px;background:var(--red);color:var(--white);text-align:center;font-style:italic;font-weight:700;font-size:18px;line-height:77px}

/* treatable */
.treat-photo{left:713px;top:1253px;width:487px;height:359px;background:linear-gradient(150deg,#f4f4f4,#d8c0ae 55%,#b59a88)}

/* testimonials */
.testimonials{left:0;top:1612px;width:1200px;height:360px;background:var(--light)}
.avatar{left:553px;top:180px;width:92px;height:92px;background:linear-gradient(#9aa6b0,#3c4754);border:3px solid var(--white)}

/* newsletter */
.newsletter{left:0;top:1972px;width:1200px;height:175px;background:linear-gradient(135deg,#d23330,#e24642 50%,#c92b28)}
.newsletter h3{position:absolute;left:174px;top:75px;color:var(--white);font-size:26px;font-weight:400}
.field{position:absolute;top:72px;height:38px;background:var(--white);font-size:12px;color:#777;padding:11px 12px}
.subscribe{position:absolute;left:926px;top:72px;width:112px;height:38px;border:2px solid var(--white);color:var(--white);font-size:12px;font-weight:600;text-align:center;line-height:34px}

/* footer */
.site-footer{left:0;top:2147px;width:1200px;height:285px;background:var(--footer);color:var(--footer-text);font-size:11px}
.site-footer h4{font-family:"Montserrat",Arial,sans-serif;color:var(--white);font-size:16px;font-weight:400}
.site-footer ul{list-style:none;line-height:19px}
.site-footer ul li:first-child{color:var(--white)}
.contact-line{display:flex;gap:8px;align-items:center;margin-top:4px}
.copyright{position:absolute;left:0;width:1200px;top:252px;text-align:center;font-size:10px}
.copyright b{color:var(--red);font-weight:600}
</style>
</head>
<body>

<header class="site-header">
  <div class="brand"><span class="brand-mark"></span>Calvexa</div>
  <div class="top-links"><span>Blog</span><span class="sep">|</span><span>Franchising</span><span class="sep">|</span><span>FAQ's</span><span class="sep">|</span><span>Contact Us</span>
    <svg width="12" height="12" viewBox="0 0 12 12"><circle cx="5" cy="5" r="3.8" fill="none" stroke="#444" stroke-width="1.6"/><line x1="8" y1="8" x2="11" y2="11" stroke="#444" stroke-width="1.8"/></svg>
  </div>
  <div class="call">Call Us: <b>+63 5550 12345</b></div>
  <nav class="nav"><span class="active">Home</span><span>Why Choose Us</span><span>Treatable Conditions</span><span>Testimonial</span><span class="quote">Request a Quote</span></nav>
</header>

<section class="abs hero" role="img" aria-label="Therapist applying a handheld laser device to a patient, treatment machine in the background">
  <h1>WE RELIEVE BODY PAIN</h1>
  <div class="rule"></div>
  <p>Lorem ipsum dolor sit amet, consectetuer adipiscing elit. Aenean commodo ligula eget dolor. Aenean massa. Cum sociis natoque penatibus et magnis.</p>
  <span class="btn">Get Started</span>
  <div class="dots" style="left:576px;top:348px"><i></i><i class="on"></i><i></i></div>
</section>

<section class="abs services">
  <svg class="abs" style="left:172px;top:140px" width="22" height="36" viewBox="0 0 22 36"><polyline points="18,2 4,18 18,34" fill="none" stroke="#fff" stroke-width="3"/></svg>
  <svg class="abs" style="left:960px;top:140px" width="22" height="36" viewBox="0 0 22 36"><polyline points="4,2 18,18 4,34" fill="none" stroke="#fff" stroke-width="3"/></svg>
  <div class="card" style="left:217px"><div class="photo" role="img" aria-label="Laser treatment on a patient's back"></div><span>Relieve Back Pain</span></div>
  <div class="card" style="left:401px"><div class="photo" role="img" aria-label="Laser treatment on a knee"></div><span>Relieve Knee Pain</span></div>
  <div class="card" style="left:586px"><div class="photo" role="img" aria-label="Shoulder treatment on a patient"></div><span>Relieve Shoulder Pain</span></div>
  <div class="card" style="left:770px"><div class="photo" role="img" aria-label="Laser treatment device"></div><span>Laser Pain Removal</span></div>
</section>

<div class="abs why-photo" role="img" aria-label="Patient wearing red protective glasses during laser treatment"></div>
<section class="abs" style="left:511px;top:860px;width:465px">
  <h2 class="section-title">Why Choose Us?</h2>
  <div class="copy" style="margin-top:34px">
    <p>Lorem ipsum dolor sit amet, consectetuer adipiscing elit. Aenean commodo ligula eget dolor. Aenean massa. Cum sociis natoque penatibus et magnis dis parturient montes, nascetur ridiculus mus. <b>Donec quam felis</b>, ultricies nec, pellentesque eu, pretium quis, sem. Nulla consequat massa quis enim.</p>
    <p>Donec pede justo, fringilla vel, aliquet nec, vulputate eget, arcu. In enim justo, rhoncus ut, imperdiet a, venenatis vitae, justo. Nullam dictum felis eu pede mollis pretium. Integer tincidunt. Cras dapibus. Vivamus elementum semper nisi. <b>Aenean vulputate</b> eleifend tellus.</p>
  </div>
</section>
<span class="btn" style="left:511px;top:1114px">Read More</span>

<div class="abs quote-band">“Under certain circumstances, profanity provides a relief denied even to prayer.”</div>

<section class="abs" style="left:233px;top:1290px;width:455px">
  <h2 class="section-title">Treatable Conditions</h2>
  <div class="copy" style="margin-top:34px">
    <p>Lorem ipsum dolor sit amet, consectetuer adipiscing elit. Aenean commodo ligula eget dolor. Aenean massa. Cum sociis natoque penatibus et magnis dis parturient montes, nascetur ridiculus mus. <b>Donec quam felis</b>, ultricies nec, pellentesque eu, pretium quis, sem. Nulla consequat massa quis enim.</p>
    <p>Donec pede justo, fringilla vel, aliquet nec, vulputate eget, arcu. In enim justo, rhoncus ut, imperdiet a, venenatis vitae, justo. Nullam dictum felis eu pede mollis pretium. Integer tincidunt. Cras dapibus. Vivamus elementum semper nisi. <b>Aenean vulputate</b> eleifend tellus.</p>
  </div>
</section>
<span class="btn" style="left:233px;top:1548px">Read More</span>
<div class="abs treat-photo" role="img" aria-label="Therapist treating a patient's upper back with a laser device"></div>

<section class="abs testimonials">
  <h2 class="section-title" style="position:absolute;left:0;width:1200px;top:36px;text-align:center">What People Say About Us?</h2>
  <p class="copy" style="position:absolute;left:330px;width:540px;top:100px;text-align:center">Lorem ipsum dolor sit amet, consectetuer adipiscing elit. Aenean commodo ligula eget dolor. Aenean massa. Cum sociis natoque penatibus et magnis dis parturient montes, nascetur ridiculus mus. Donec quam felis, ultricies nec, pellentesque eu, pretium quis, sem.</p>
  <div class="abs avatar" role="img" aria-label="Portrait of the client giving the testimonial"></div>
  <div style="position:absolute;left:0;width:1200px;top:280px;text-align:center;font-family:Montserrat,Arial,sans-serif;font-size:16px;font-weight:600;color:var(--ink)">John Doe</div>
  <div style="position:absolute;left:0;width:1200px;top:302px;text-align:center;font-size:11px;color:#666">Manager</div>
  <div class="dots" style="left:576px;top:331px"><i style="border-color:var(--red);background:none"></i><i class="on" style="border-color:var(--red)"></i><i style="border-color:var(--red);background:none"></i></div>
</section>

<section class="abs newsletter">
  <h3>SUBSCRIBE TO NEWSLETTER</h3>
  <div class="field" style="left:566px;width:166px">Name</div>
  <div class="field" style="left:746px;width:166px">Email</div>
  <div class="subscribe">Subscribe</div>
</section>

<footer class="abs site-footer">
  <div class="abs" style="left:235px;top:46px;width:230px">
    <h4>About Us</h4>
    <p style="margin-top:22px;line-height:17px">Lorem ipsum dolor sit amet, consectetuer adipiscing elit. Aenean commodo ligula eget dolor. Aenean massa. Cum sociis natoque penatibus et magnis dis parturient montes, nascetur ridiculus mus. Donec quam felis, ultricies nec, pellentesque eu, pretium quis, sem.</p>
  </div>
  <div class="abs" style="left:580px;top:46px">
    <h4>Quick Links</h4>
    <ul style="margin-top:22px"><li>Home</li><li>Why Choose Us</li><li>Treatable Conditions</li><li>Testimonial</li><li>Blog</li><li>Franchising</li><li>FAQs</li><li>Contact Us</li></ul>
  </div>
  <div class="abs" style="left:839px;top:46px">
    <h4>Contact Info</h4>
    <ul style="margin-top:22px;line-height:17px"><li style="color:var(--footer-text)">Address Street Here</li><li>Address Municipality Here</li><li>Address City Here</li><li>Zipcode Here</li></ul>
    <div class="contact-line" style="margin-top:14px"><svg width="12" height="9" viewBox="0 0 12 9"><rect width="12" height="9" fill="var(--red)"/><polyline points="0,0 6,5 12,0" fill="none" stroke="#fff"/></svg><span style="color:#fff">info@calvexamail.com</span></div>
    <div class="contact-line"><svg width="12" height="12" viewBox="0 0 12 12"><path d="M2 1l3 2-1 2c1 1.5 2 2.5 3 3l2-1 2 3-2 1C5 10 2 7 1 3z" fill="var(--red)"/></svg><span style="color:#fff">+123 555 019</span></div>
  </div>
  <div class="copyright">Copyright 2015. <b>Calvexa</b>. All Rights Reserved.</div>
</footer>

</body>
</html>
```